New Flyer Design Project for Theatre School - Performing Arts

I am looking for a band new 2 sided leaflet for my theatre school - A5 size ( double sided)

The leaflet should appeal to a decrease mix of children and parents, look fun yet professional and appeal to boys and well as girls. Please can it not look too cluttered.

The leaflet should mention classes and locations;
Wrenley Village
New Bramwick

It should mention that we have a hugely successful FREE casting agency for all pupils and show their photo's with recent credits ( photo's below)

Please include the photos and credits of the children listed here (photos below)

Rosalind - The Lanterns at The Harbour Playhouse
Barnaby - Lead role in a brand new QRN TV series
Teddy - Major TV commercial
Rupert - Lead role of Teddy un Milo And The Marble Lighthouse - Corner Theatre
Morwenna - Pantomime - Ashgrove Rooms
Ottilie - Major TV commercial
Briony - Lead role in West End Play Paper Kites
Imogen- Major TV commercial
Fergus - Role in a Major QRN series
Hazel - Short film

I attach previous leaflets with information on.
Website is www.brightwingstudio.co.uk

All logo's are attached ( BWS Star, PVKR, OSLE and FRENOK) Please include all

Note; We are accredited with the Guild of Movement, Voice and Stagecraft

Classes are award winning, accredited and affordable.

Classes include;
FRENOK
Drama
Improvisation
Audition Technique
Singing
Musical Theatre
Tap
Ballet

Ages are 3-18years

** We are now in our successful 21st Year***

I have attached a selection of photos for your use, the photos included should show a mixture of ages and ethnicities and an equal mix of girls and boys please

Theatre and performing Arts

Sans Serif

0054AA
0677BA
7BADD7
CADEEF
E8F1F8
FFC000
F8CF3A
FAE287
FDF2CF
FEFAEE
6B429C
8869AF
B7A5CE
E3DAEB
F3F0F8

```html
<!DOCTYPE html>
<html lang="en">
<head>
<meta charset="utf-8">
<title>Brightwing Studio – Theatre School Leaflet</title>
<link href="https://fonts.googleapis.com/css2?family=Montserrat:wght@500;600;700;800;900&display=swap" rel="stylesheet">
<style>
  :root {
    --ink: #000000;
    --red: #e3101f;
    --yellow: #f6d63a;
    --purple: #7a2a9c;
    --navy: #2f4c9c;
    --canvas: #e8e8ea;
    --white: #ffffff;
  }
  * { box-sizing: border-box; margin: 0; padding: 0; }
  html, body { width: 1200px; height: 792px; overflow: hidden; }
  body {
    background: var(--canvas);
    font-family: "Montserrat", sans-serif;
    color: var(--yellow);
    position: relative;
  }
  .page {
    position: absolute;
    top: 16px;
    width: 537px;
    height: 760px;
    background: var(--ink);
    overflow: hidden;
  }
  .page--front { left: 42px; }
  .page--back { left: 621px; }
  .abs { position: absolute; }

  /* ---------- front ---------- */
  .hero-photo {
    left: 0; top: 0; width: 537px; height: 170px;
    background: linear-gradient(100deg, #1a0606 0%, #5a1410 35%, #8a1d18 60%, #3a0c0a 100%);
  }
  .brand {
    left: 16px; top: 22px;
    display: flex; align-items: center; gap: 10px;
  }
  .brand__mark {
    width: 40px; height: 40px; border-radius: 50%;
    background: var(--yellow);
  }
  .brand__name {
    font-weight: 800; font-size: 22px; color: var(--yellow);
    line-height: 1.05; width: 120px;
  }
  .headshots {
    left: 0; top: 170px; width: 537px; height: 86px;
    display: flex; gap: 3px; background: var(--ink);
  }
  .headshots span {
    flex: 1;
    background: linear-gradient(180deg, #1d2d52 0%, #0c1530 100%);
  }
  .banner-red {
    background: var(--red);
    border-radius: 10px;
    font-weight: 900;
    text-align: center;
    color: var(--yellow);
  }
  .tagline {
    left: 30px; top: 268px; width: 477px; height: 64px;
    font-size: 18.5px; line-height: 1.35; letter-spacing: 0.8px;
    padding-top: 7px;
  }
  .anniversary {
    left: 0; top: 344px; width: 537px;
    text-align: center; font-weight: 900; font-size: 23px; line-height: 1.4;
    letter-spacing: 0.5px;
  }
  .classes {
    left: 44px; top: 422px; width: 449px; height: 112px;
    border: 4px solid var(--red); border-radius: 18px;
    display: grid; grid-template-columns: 1.1fr 1fr;
    padding: 12px 14px 0 16px;
  }
  .classes ul { list-style: none; }
  .classes li {
    font-weight: 500; font-size: 15.5px; line-height: 1.4; letter-spacing: 0.3px;
    display: flex; align-items: center; gap: 7px;
  }
  .star-bullet { width: 11px; height: 11px; fill: var(--red); flex: none; }
  .venue {
    top: 546px; height: 30px;
    background: var(--red); border-radius: 4px;
    display: flex; align-items: center; gap: 10px; padding: 0 14px;
    font-weight: 900; font-size: 16px; letter-spacing: 0.6px;
    white-space: nowrap;
  }
  .venue--first { left: 40px; width: 230px; }
  .venue--second { left: 296px; width: 204px; }
  .pin-badge {
    width: 20px; height: 20px; border-radius: 50%; background: var(--yellow);
    display: flex; align-items: center; justify-content: center; flex: none;
  }
  .pin-badge svg { width: 12px; height: 12px; fill: var(--red); }
  .cta-trial {
    left: 104px; top: 588px; width: 330px; height: 42px;
    font-size: 24px; line-height: 42px; border-radius: 4px;
  }
  .web {
    left: 0; top: 638px; width: 537px; text-align: center;
    font-weight: 900; font-size: 16px; letter-spacing: 0.5px;
  }
  .badge { position: absolute; }
  .badge--exams { left: 40px; top: 676px; width: 152px; height: 84px; background: var(--purple); }
  .badge--awards { left: 205px; top: 692px; width: 150px; height: 56px; background: var(--white); border: 3px solid var(--navy); }
  .badge--dance { left: 378px; top: 676px; width: 118px; height: 84px; background: var(--purple); }

  /* ---------- back ---------- */
  .stage-photo {
    left: 0; top: 0; width: 537px; height: 340px;
    background: linear-gradient(160deg, #0a0614 0%, #2a0f3a 45%, #5c1422 75%, #1a0a24 100%);
  }
  .credits {
    left: 12px; top: 12px; list-style: none; width: 280px;
  }
  .credits li {
    font-size: 7.6px; font-weight: 600; line-height: 1.25;
    display: flex; gap: 7px; margin-bottom: 10px; letter-spacing: 0.2px;
  }
  .credits li .star-bullet { fill: var(--yellow); width: 10px; height: 10px; margin-top: -1px; }
  .credits b { font-weight: 800; }
  .star-frames { left: 250px; top: 10px; width: 287px; height: 450px; }
  .snap { top: 358px; height: 88px; }
  .snap--one { left: 12px; width: 122px; background: linear-gradient(180deg, #1c2aa0 0%, #0e1450 100%); }
  .snap--two { left: 140px; width: 116px; background: linear-gradient(180deg, #d8603a 0%, #6a1a2a 100%); }
  .ages {
    left: 56px; top: 468px; width: 430px; height: 50px;
    font-size: 29px; line-height: 50px; border-radius: 6px; letter-spacing: 0.5px;
  }
  .casting {
    left: 20px; top: 534px; width: 497px; text-align: center;
    font-weight: 800; font-size: 11.5px; line-height: 1.9; letter-spacing: 0.3px;
  }
  .note {
    left: 40px; top: 592px; width: 480px;
    display: flex; align-items: center; gap: 10px;
  }
  .note__label { font-weight: 900; font-size: 15px; }
  .note__text { font-weight: 800; font-size: 10.5px; line-height: 1.5; letter-spacing: 0.2px; }
  .finale-photo {
    left: 322px; top: 640px; width: 215px; height: 100px;
    background: linear-gradient(180deg, #2a0a4a 0%, #6a1aa0 70%, #3a0a5a 100%);
  }
  .contact { left: 40px; top: 646px; width: 278px; }
  .contact__trial { font-weight: 900; font-size: 17px; margin-bottom: 8px; }
  .contact__row {
    display: flex; align-items: center; gap: 8px;
    font-weight: 900; font-size: 14px; margin-bottom: 7px; letter-spacing: 0.3px;
    white-space: nowrap;
  }
  .contact__row--web { font-size: 12.5px; letter-spacing: 0; }
  .icon-dot {
    width: 18px; height: 18px; border-radius: 50%; background: var(--red);
    display: flex; align-items: center; justify-content: center; flex: none;
  }
  .icon-dot svg { width: 10px; height: 10px; fill: var(--ink); }
</style>
</head>
<body>
  <svg width="0" height="0" style="position:absolute">
    <defs>
      <symbol id="star" viewBox="0 0 24 24"><polygon points="12,1 15,9 23.5,9 16.7,14 19.3,22.5 12,17.4 4.7,22.5 7.3,14 0.5,9 9,9"/></symbol>
      <symbol id="pin" viewBox="0 0 24 24"><path d="M12 1a8 8 0 0 0-8 8c0 6 8 14 8 14s8-8 8-14a8 8 0 0 0-8-8zm0 11a3 3 0 1 1 0-6 3 3 0 0 1 0 6z"/></symbol>
      <symbol id="mail" viewBox="0 0 24 24"><path d="M2 5h20v14H2zM3.5 6.5l8.5 6.5 8.5-6.5v-.5h-17z"/></symbol>
    </defs>
  </svg>

  <!-- Front side -->
  <section class="page page--front">
    <div class="abs hero-photo" role="img" aria-label="Stage photo of young performers in red jackets dancing"></div>
    <div class="abs brand">
      <span class="brand__mark"></span>
      <span class="brand__name">Brightwing Studio</span>
    </div>
    <div class="abs headshots" role="img" aria-label="Row of seven pupil headshot portraits">
      <span></span><span></span><span></span><span></span><span></span><span></span><span></span>
    </div>

    <p class="abs banner-red tagline">CLASSES ARE AWARD WINNING,<br>ACCREDITED AND AFFORDABLE</p>
    <p class="abs anniversary">WE ARE NOW<br>IN OUR SUCCESSFUL 21ST YEAR</p>

    <div class="abs classes">
      <ul>
        <li><svg class="star-bullet"><use href="#star"/></svg>FRENOK</li>
        <li><svg class="star-bullet"><use href="#star"/></svg>DRAMA</li>
        <li><svg class="star-bullet"><use href="#star"/></svg>IMPROVISATION</li>
        <li><svg class="star-bullet"><use href="#star"/></svg>AUDITION TECHNIQUE</li>
      </ul>
      <ul>
        <li><svg class="star-bullet"><use href="#star"/></svg>SINGING</li>
        <li><svg class="star-bullet"><use href="#star"/></svg>MUSICAL THEATRE</li>
        <li><svg class="star-bullet"><use href="#star"/></svg>TAP</li>
        <li><svg class="star-bullet"><use href="#star"/></svg>BALLET</li>
      </ul>
    </div>

    <div class="abs venue venue--first"><span class="pin-badge"><svg><use href="#pin"/></svg></span>WRENLEY VILLAGE</div>
    <div class="abs venue venue--second"><span class="pin-badge"><svg><use href="#pin"/></svg></span>NEW BRAMWICK</div>

    <p class="abs banner-red cta-trial">"Book a Trial TODAY!'</p>
    <p class="abs web">www.brightwingstudio.co.uk</p>

    <div class="badge badge--exams" role="img" aria-label="FRENOK exams badge"></div>
    <div class="badge badge--awards" role="img" aria-label="PVKR recognised school badge"></div>
    <div class="badge badge--dance" role="img" aria-label="OSLE dance teachers badge"></div>
  </section>

  <!-- Back side -->
  <section class="page page--back">
    <div class="abs stage-photo" role="img" aria-label="Stage photo of pupils in red and black school costumes performing"></div>

    <ul class="abs credits">
      <li><svg class="star-bullet"><use href="#star"/></svg><span><b>ROSALIND</b> - THE LANTERNS AT THE HARBOUR PLAYHOUSE</span></li>
      <li><svg class="star-bullet"><use href="#star"/></svg><span><b>BARNABY</b> - LEAD ROLE IN A BRAND NEW QRN TV SERIES</span></li>
      <li><svg class="star-bullet"><use href="#star"/></svg><span><b>TEDDY</b> - MAJOR TV COMMERCIAL</span></li>
      <li><svg class="star-bullet"><use href="#star"/></svg><span><b>RUPERT</b> - LEAD ROLE OF TEDDY UN MILO<br>AND THE MARBLE LIGHTHOUSE - CORNER THEATRE</span></li>
      <li><svg class="star-bullet"><use href="#star"/></svg><span><b>MORWENNA</b> - PANTOMIME - ASHGROVE ROOMS</span></li>
      <li><svg class="star-bullet"><use href="#star"/></svg><span><b>OTTILIE</b> - MAJOR TV COMMERCIAL</span></li>
      <li><svg class="star-bullet"><use href="#star"/></svg><span><b>BRIONY</b> - LEAD ROLE IN WEST END PLAY PAPER KITES</span></li>
      <li><svg class="star-bullet"><use href="#star"/></svg><span><b>IMOGEN</b>- MAJOR TV COMMERCIAL</span></li>
      <li><svg class="star-bullet"><use href="#star"/></svg><span><b>FERGUS</b> - ROLE IN A MAJOR QRN SERIES</span></li>
      <li><svg class="star-bullet"><use href="#star"/></svg><span><b>HAZEL</b> - SHORT FILM</span></li>
    </ul>

    <svg class="abs star-frames" viewBox="0 0 287 450" role="img" aria-label="Three star-shaped frames holding stage photos of pupils">
      <defs>
        <linearGradient id="starFill" x1="0" y1="0" x2="0" y2="1">
          <stop offset="0" stop-color="#6a6f8a"/>
          <stop offset="1" stop-color="#2a2238"/>
        </linearGradient>
      </defs>
      <g fill="url(#starFill)" stroke="#f6d63a" stroke-width="3" stroke-linejoin="miter">
        <polygon points="210,5 226,60 282,60 237,94 255,150 210,116 165,150 183,94 138,60 194,60"/>
        <polygon points="115,145 131,198 186,198 142,230 158,282 115,250 72,282 88,230 44,198 99,198"/>
        <polygon points="211,278 227,333 282,333 238,367 256,422 211,388 166,422 184,367 140,333 195,333"/>
      </g>
    </svg>

    <div class="abs snap snap--one" role="img" aria-label="Stage photo of a cast in colourful costumes"></div>
    <div class="abs snap snap--two" role="img" aria-label="Stage photo of a dance group under orange lights"></div>

    <p class="abs banner-red ages">AGES ARE 3-18YEARS</p>
    <p class="abs casting">WE HAVE A HUGELY SUCCESSFUL FREE CASTING AGENCY<br>FOR ALL PUPILS AND SHOW THEIR</p>
    <div class="abs note">
      <span class="note__label">NOTE;</span>
      <span class="note__text">WE ARE ACCREDITED WITH THE GUILD OF MOVEMENT,<br>VOICE AND STAGECRAFT</span>
    </div>

    <div class="abs finale-photo" role="img" aria-label="Stage photo of pupils in striped costumes dancing with arms raised"></div>
    <div class="abs contact">
      <p class="contact__trial">"Book a Trial TODAY!'</p>
      <p class="contact__row"><span class="icon-dot"><svg><use href="#pin"/></svg></span>WRENLEY VILLAGE</p>
      <p class="contact__row"><span class="icon-dot"><svg><use href="#pin"/></svg></span>NEW BRAMWICK</p>
      <p class="contact__row contact__row--web"><span class="icon-dot"><svg><use href="#mail"/></svg></span>www.brightwingstudio.co.uk</p>
    </div>
  </section>
</body>
</html>
```